New Business Card Design Project

The legal name of the company is TTTolvane, we also refer to it as simply Tolvane or you could also use the initials TTT...... please feel creative.
Excellent design.
On the second side, if you could image North and South America on each drop of water ... it almost looks like that now.
The website is www.tttolvane-example.com
Attached is another card with the required information; no addresses.

Industry/Entity Type

Legal

```html
<!DOCTYPE html>
<html lang="en">
<head>
<meta charset="utf-8">
<title>Tolvane Business Card</title>
<link rel="stylesheet" href="https://fonts.googleapis.com/css2?family=Noto+Sans:wght@400;700&display=swap">
<style>
  :root {
    --page-bg: #e7e4df;
    --card-black: #111111;
    --card-texture: #1b1b1b;
    --ink-white: #f2f2f2;
    --ink-soft: #d0d0d0;
    --photo-dark: #2a2a2a;
    --photo-mid: #7d7b79;
    --photo-light: #c9c6c2;
  }
  * { margin: 0; padding: 0; box-sizing: border-box; }
  html, body {
    width: 924px;
    height: 1200px;
    overflow: hidden;
    background: var(--page-bg);
    font-family: "Noto Sans", Verdana, sans-serif;
  }
  .stage { position: relative; width: 924px; height: 1200px; }
  .card {
    position: absolute;
    left: 102px;
    width: 720px;
    height: 410px;
    background-color: var(--card-black);
    background-image:
      repeating-linear-gradient(0deg, var(--card-texture) 0 1px, transparent 1px 3px),
      repeating-linear-gradient(90deg, var(--card-texture) 0 1px, transparent 1px 3px);
    box-shadow: 0 6px 18px rgba(0,0,0,0.25);
    color: var(--ink-white);
  }
  .card--back { top: 150px; }
  .card--front { top: 640px; }

  .back-photo {
    position: absolute;
    left: 48px;
    top: 62px;
    right: 0;
    height: 270px;
    background:
      radial-gradient(ellipse 30% 40% at 62% 52%, var(--photo-light), transparent 70%),
      linear-gradient(170deg, var(--photo-dark) 0%, var(--photo-mid) 45%, var(--photo-light) 60%, var(--photo-mid) 75%, var(--photo-dark) 100%);
  }
  .back-website {
    position: absolute;
    right: 40px;
    top: 348px;
    font-size: 15px;
    letter-spacing: 3px;
    color: var(--ink-soft);
  }

  .contact-list {
    position: absolute;
    left: 36px;
    top: 42px;
    list-style: none;
    font-size: 15px;
    line-height: 22px;
    color: var(--ink-soft);
  }
  .brand {
    position: absolute;
    left: 262px;
    top: 150px;
  }
  .brand__name {
    font-size: 30px;
    font-weight: 700;
    letter-spacing: 1px;
    line-height: 1;
    text-align: center;
  }
  .brand__legal {
    font-size: 27px;
    font-weight: 400;
    line-height: 1.2;
    margin-top: 4px;
  }
  .person {
    position: absolute;
    right: 44px;
    bottom: 42px;
    text-align: right;
  }
  .person__name { font-size: 19px; font-weight: 700; }
  .person__role { font-size: 16px; color: var(--ink-soft); }
</style>
</head>
<body>
<main class="stage">
  <section class="card card--back" aria-label="Card back">
    <div class="back-photo" role="img" aria-label="Close-up photograph of a water drop splashing into a dark pool"></div>
    <p class="back-website">www.tttolvane-example.com</p>
  </section>

  <section class="card card--front" aria-label="Card front">
    <ul class="contact-list">
      <li>USA: +1 (555) 014 2290</li>
      <li>Guatemala: +502 5550 0184</li>
      <li>info@tttolvane-example.com</li>
      <li>www.tttolvane-example.com</li>
    </ul>
    <div class="brand">
      <p class="brand__name">TOLVANE</p>
      <p class="brand__legal">tttolvane sa, llc</p>
    </div>
    <div class="person">
      <p class="person__name">Leon Varga</p>
      <p class="person__role">Managing Director</p>
    </div>
  </section>
</main>
</body>
</html>
```